A front Sign for The Kelverton Orthopaedic Centre

A sign for the front of our consulting rooms. Utilising logo winner of competition 3757477. Business card and letterhead competition 3793183. Specialist Orthopaedic surgeons. includes a phone number.

```html
<!DOCTYPE html>
<html lang="en">
<head>
<meta charset="utf-8">
<title>The Kelverton Orthopaedic Centre – Front Sign</title>
<link rel="stylesheet" href="https://fonts.googleapis.com/css2?family=Questrial&family=Poppins:ital,wght@1,800&display=swap">
<style>
  :root {
    --page: #ffffff;
    --frame: #9a9a9a;
    --ink: #1b1716;
    --brand-blue: #0b6aad;
    --band-blue: #0aa6dd;
    --deep-blue: #0a1f8a;
    --glow-blue: #16c8f2;
    --gold: #e6a93b;
    --white: #ffffff;
  }
  html, body {
    margin: 0;
    padding: 0;
    width: 1200px;
    height: 1200px;
    overflow: hidden;
    background: var(--page);
  }
  .canvas {
    position: relative;
    width: 1198px;
    height: 1198px;
    border: 1px solid #b5b5b5;
    background: var(--page);
  }
  .sign {
    position: absolute;
    left: 16px;
    top: 284px;
    width: 1168px;
    height: 632px;
    border: 1px solid var(--frame);
    box-sizing: border-box;
    overflow: hidden;
    background: var(--white);
  }
  .sign-art {
    position: absolute;
    inset: 0;
    width: 100%;
    height: 100%;
  }
  .logo-box {
    position: absolute;
    left: 102px;
    top: 28px;
    width: 422px;
    height: 140px;
    border: 1px solid var(--frame);
    box-sizing: border-box;
    display: flex;
    align-items: center;
    justify-content: center;
    text-align: center;
    font-family: "Questrial", sans-serif;
    font-size: 34px;
    line-height: 1.15;
    color: var(--ink);
  }
  .headline-lead {
    position: absolute;
    left: 60px;
    top: 184px;
    margin: 0;
    font-family: "Questrial", sans-serif;
    font-weight: 400;
    font-size: 98px;
    line-height: 1;
    color: var(--ink);
  }
  .headline-main {
    position: absolute;
    left: 70px;
    top: 296px;
    margin: 0;
    font-family: "Poppins", sans-serif;
    font-style: italic;
    font-weight: 800;
    font-size: 94px;
    line-height: 112px;
    color: var(--brand-blue);
  }
  .call-now {
    position: absolute;
    left: 84px;
    top: 554px;
    font-family: "Poppins", sans-serif;
    font-style: italic;
    font-weight: 800;
    font-size: 36px;
    line-height: 1;
    color: var(--white);
  }
  .phone {
    position: absolute;
    left: 302px;
    top: 536px;
    font-family: "Poppins", sans-serif;
    font-style: italic;
    font-weight: 800;
    font-size: 74px;
    line-height: 1;
    color: var(--white);
  }
</style>
</head>
<body>
<div class="canvas">
  <div class="sign">
    <svg class="sign-art" viewBox="20 355 1460 790" preserveAspectRatio="none" xmlns="http://www.w3.org/2000/svg">
      <defs>
        <radialGradient id="anatomy-glow" cx="0.45" cy="0.5" r="0.7">
          <stop offset="0" stop-color="var(--glow-blue)"/>
          <stop offset="0.55" stop-color="#0a6fd0"/>
          <stop offset="1" stop-color="var(--deep-blue)"/>
        </radialGradient>
      </defs>
      <polygon class="call-ribbon" points="88,1027 1060,1027 1060,1113 88,1113 112,1070" fill="var(--gold)"/>
      <path class="accent-arc" d="M810,355 Q1210,750 910,1145 L1480,1145 L1480,355 Z" fill="var(--band-blue)"/>
      <path class="anatomy-panel" d="M905,355 Q1225,750 915,1145 L1480,1145 L1480,355 Z" fill="url(#anatomy-glow)" role="img" aria-label="Illustration of a running man with skeleton and highlighted joints at shoulder, elbow, wrist, hip, knee and ankle"/>
    </svg>

    <div class="logo-box">The Kelverton<br>Orthopaedic Centre</div>

    <h2 class="headline-lead">Specialist</h2>
    <h1 class="headline-main">Orthopaedic<br>Surgeons</h1>

    <span class="call-now">Call Now</span>
    <span class="phone">123.456.789</span>
  </div>
</div>
</body>
</html>
```